Website Design & Development For a New Start Up

We require a bespoke website design and development.
Requirements:
We want something similar to www.quillharbor.com... not exact as this is copywrite infringement... but we want you to get a feel for the site and design accordingly. We will leave the creativity to you.
All logos, detailed content and description will be given upon seeing the designs and your eye for creativity. here are our requirements.
1. Upto 20 internal pages. Clean simple design that will be discussed with developer.
2. Account Opening sections - Very detailed client sign up. 4 types of client to sign up (Bespoke account information required for each client)
3. Client Login Area. Client Authentication tools.
4. Admin and Client area - where documents and information will be stored.
5. Live API currency feeds into front end.
6. Document security and Website security is very important as we will be holding client information
7. We want the website to be RESPONSIVE on ALL smart Phones and Zentabs etc. Website MUST work on all browsers regardless of age.
8. We would like ALL coding to be done in CLEAN HTML5 and it must work effortlessly for clients when they touch any button etc.
We want a designer and developer that has the eye for intricate aesthetic design and technical ability to execute functional perfectly and make the user experience effortless.
We look forward to seeing your designs and working with you.
Regards
Brelka Team
Reason: We are still getting designs and we have yet to get it perfected so we are waiting for more submissions. Thanks
Financial Money Transaction
Security

```html
<!DOCTYPE html>
<html lang="en">
<head>
<meta charset="utf-8">
<title>Sendora — Save money through sending</title>
<link href="https://fonts.googleapis.com/css2?family=Open+Sans:wght@300;400;600;700&display=swap" rel="stylesheet">
<style>
:root{
  --blue:#1aa0d8;
  --blue-dark:#1089bd;
  --ink:#2f3337;
  --muted:#7a7f85;
  --line:#e3e6e9;
  --cream:#f8f7ef;
  --white:#ffffff;
  --footer:#1d2126;
}
*{box-sizing:border-box;margin:0;padding:0}
html,body{width:1200px;height:3024px;overflow:hidden}
body{font-family:"Open Sans",Arial,sans-serif;color:var(--ink);background:var(--white)}
.page{width:1200px;height:3024px;position:relative}

/* hero */
.hero{position:relative;height:540px;overflow:hidden}
.hero-photo{position:absolute;inset:0;background:linear-gradient(120deg,#c9a58a 0%,#e8d2c0 35%,#9fb9c9 65%,#b3866c 100%)}
.nav{position:absolute;top:0;left:0;right:0;height:62px;display:flex;align-items:center;padding:0 44px;background:rgba(255,255,255,.12)}
.brand{font-size:26px;font-weight:700;color:var(--white);letter-spacing:1px}
.lang{margin-left:18px;color:var(--white);font-size:12px}
.nav-links{margin-left:auto;display:flex;gap:34px;align-items:center;font-size:13px;font-weight:600;color:var(--white)}
.nav-cta{background:var(--blue);padding:9px 18px;border-radius:2px}
.send-card{position:absolute;left:460px;top:118px;width:300px;height:400px;background:rgba(255,255,255,.9);padding:22px 26px;text-align:center}
.send-card h1{font-size:19px;font-weight:700;line-height:1.35;text-transform:uppercase;color:var(--ink)}
.field{margin-top:14px;text-align:left}
.field label{font-size:12px;color:var(--muted)}
.field-row{display:flex;margin-top:4px;height:34px;border:1px solid var(--line);background:var(--white)}
.field-row span{flex:1;padding:7px 10px;font-size:14px}
.field-row b{width:70px;background:var(--blue);color:var(--white);font-size:13px;display:flex;align-items:center;justify-content:center}
.save-note{margin-top:10px;font-size:11px;color:var(--blue)}
.btn{display:inline-block;background:var(--blue);color:var(--white);font-size:14px;font-weight:700;text-transform:uppercase;padding:11px 26px;border-radius:2px}
.send-card .btn{margin-top:12px;width:100%}
.rate{margin-top:10px;font-size:11px;color:var(--muted)}
.badges{margin-top:10px;display:flex;gap:8px;justify-content:center}
.badges i{width:72px;height:20px;background:#cfd6dc;border-radius:2px}

/* features */
.features{height:320px;display:flex;justify-content:center;gap:90px;padding-top:56px}
.feature{width:150px;text-align:center}
.feature-icon{width:150px;height:150px;background:var(--blue);display:flex;align-items:center;justify-content:center}
.feature h3{margin-top:16px;font-size:15px;font-weight:700;text-transform:uppercase}
.feature p{margin-top:6px;font-size:11px;color:var(--muted);line-height:1.45}

/* easy */
.easy{height:460px;display:flex;padding:60px 40px 0 140px;border-top:1px solid var(--line)}
.easy-text{width:520px}
.easy-text h2{font-size:26px;font-weight:400;text-transform:uppercase;color:var(--ink)}
.easy-text p{margin-top:14px;font-size:12px;color:var(--muted);line-height:1.6}
.easy-text .btn{margin-top:22px;font-size:13px;padding:10px 22px}
.easy-photo{margin-left:40px;width:500px;height:360px;background:linear-gradient(135deg,#e9e3dc,#cfae94 55%,#efe9e2)}

/* trust band */
.trust{height:170px;background:var(--blue);color:var(--white);text-align:center;padding-top:34px}
.trust h2{font-size:26px;font-weight:700;text-transform:uppercase}
.trust .amount{margin-top:8px;font-size:40px;font-weight:300}
.trust small{font-size:12px;opacity:.85}

/* testimonials */
.customers{height:550px;text-align:center;padding-top:56px}
.section-title{font-size:30px;font-weight:400;text-transform:uppercase}
.section-intro{width:620px;margin:10px auto 0;font-size:12px;color:var(--muted);line-height:1.55}
.quotes{display:flex;justify-content:center;gap:52px;margin-top:40px}
.quote{width:200px}
.avatar{width:108px;height:108px;border-radius:50%;margin:0 auto;background:linear-gradient(160deg,#c9cfd4,#8c969e)}
.quote h4{margin-top:16px;font-size:17px;font-weight:400}
.quote p{margin-top:8px;font-size:11px;color:var(--muted);line-height:1.5}
.customers .btn{margin-top:36px;font-size:13px;padding:10px 22px}

/* stats */
.stats{height:440px;background:var(--cream);padding-top:46px;text-align:center}
.stats-body{display:flex;justify-content:center;gap:60px;margin-top:30px;text-align:left}
.stats-list{list-style:none;width:430px}
.stats-list li{font-size:16px;padding:13px 0 13px 60px;border-bottom:1px solid var(--line);position:relative}
.stats-list li::before{content:"›";position:absolute;left:26px;top:8px;font-size:22px;color:var(--ink)}

/* world */
.world{height:480px;background:var(--blue);text-align:center;padding-top:44px;color:var(--white)}
.world .section-title{font-size:28px}
.world .section-intro{color:rgba(255,255,255,.8)}
.world-map{width:720px;height:300px;margin:22px auto 0;background:linear-gradient(180deg,rgba(255,255,255,.35),rgba(255,255,255,.18));border-radius:40px}

/* footer */
.footer{height:64px;background:var(--footer);display:flex;align-items:center;padding:0 160px;color:#c9ced3;font-size:11px}
.social{margin-left:auto;display:flex;gap:18px}
.social i{width:18px;height:18px;border-radius:50%;background:#c9ced3}
</style>
</head>
<body>
<div class="page">

  <header class="hero">
    <div class="hero-photo" role="img" aria-label="Photo of a smiling young girl outdoors with soft bokeh lights"></div>
    <nav class="nav">
      <span class="brand">SENDORA</span>
      <span class="lang">EN ▾</span>
      <div class="nav-links">
        <span>SIGN UP</span><span>LOGIN</span><span>HELP ▾</span>
        <span class="nav-cta">SEND MONEY</span>
      </div>
    </nav>
    <form class="send-card">
      <h1>Save money<br>through sending</h1>
      <div class="field">
        <label>You send</label>
        <div class="field-row"><span>1000</span><b>EUR ▾</b></div>
      </div>
      <div class="field">
        <label>Recipient gets</label>
        <div class="field-row"><span>1,013.25</span><b>GBP ▾</b></div>
      </div>
      <p class="save-note">You can save £23 with us today</p>
      <span class="btn">Get started</span>
      <p class="rate">1 EUR = 0.7732 GBP</p>
      <div class="badges"><i></i><i></i><i></i></div>
    </form>
  </header>

  <section class="features">
    <div class="feature">
      <div class="feature-icon">
        <svg width="70" height="60" viewBox="0 0 70 60" fill="none" stroke="#fff" stroke-width="4"><ellipse cx="34" cy="32" rx="26" ry="20"/><line x1="20" y1="50" x2="20" y2="58"/><line x1="46" y1="50" x2="46" y2="58"/><line x1="28" y1="18" x2="40" y2="18"/></svg>
      </div>
      <h3>Low cost</h3>
      <p>Low fees displayed up front, no hidden extras ever added.</p>
    </div>
    <div class="feature">
      <div class="feature-icon">
        <svg width="70" height="60" viewBox="0 0 70 60" fill="none" stroke="#fff" stroke-width="4"><polyline points="30,10 50,30 30,50"/><line x1="6" y1="20" x2="24" y2="20"/><line x1="2" y1="30" x2="24" y2="30"/><line x1="6" y1="40" x2="24" y2="40"/></svg>
      </div>
      <h3>Fastest</h3>
      <p>Transfers arrive quickly, most within one working day.</p>
    </div>
    <div class="feature">
      <div class="feature-icon">
        <svg width="70" height="60" viewBox="0 0 70 60" fill="none" stroke="#fff" stroke-width="4"><rect x="6" y="8" width="58" height="44" rx="3"/><text x="35" y="40" fill="#fff" stroke="none" font-size="26" font-weight="700" text-anchor="middle" font-family="Open Sans, sans-serif">$</text></svg>
      </div>
      <h3>Easy and safe</h3>
      <p>A few simple steps and your money is on its way.</p>
    </div>
    <div class="feature">
      <div class="feature-icon">
        <svg width="60" height="64" viewBox="0 0 60 64" fill="none" stroke="#fff" stroke-width="4"><path d="M30 4 L54 14 V32 C54 46 42 56 30 60 C18 56 6 46 6 32 V14 Z"/><polyline points="19,32 27,40 42,24"/></svg>
      </div>
      <h3>Secured</h3>
      <p>Your data is protected with bank level encryption.</p>
    </div>
  </section>

  <section class="easy">
    <div class="easy-text">
      <h2>Sending money with us is easy!</h2>
      <p>Lorem ipsum dolor sit amet, consectetur adipiscing elit, sed do eiusmod tempor incididunt ut labore et dolore magna aliqua. Ut enim ad minim veniam, quis nostrud exercitation ullamco laboris nisi ut aliquip ex ea commodo consequat duis aute irure.</p>
      <p>Dolor in reprehenderit in voluptate velit esse cillum dolore eu fugiat nulla pariatur. Excepteur sint occaecat cupidatat non proident, sunt in culpa qui officia deserunt mollit anim id est laborum sed perspiciatis.</p>
      <p>Unde omnis iste natus error sit voluptatem accusantium doloremque laudantium, totam rem aperiam eaque ipsa quae ab illo inventore veritatis.</p>
      <span class="btn">Get started</span>
    </div>
    <div class="easy-photo" role="img" aria-label="Photo of a happy family of three smiling together"></div>
  </section>

  <section class="trust">
    <h2>A brand you can trust</h2>
    <div class="amount">$150,035,064,034</div>
    <small>Transferred</small>
  </section>

  <section class="customers">
    <h2 class="section-title">What our customers says</h2>
    <p class="section-intro">Lorem ipsum dolor sit amet, consectetur adipiscing elit, sed do eiusmod tempor incididunt ut labore et dolore magna.</p>
    <div class="quotes">
      <div class="quote">
        <div class="avatar" role="img" aria-label="Portrait photo of customer Marcus Tellan"></div>
        <h4>Marcus Tellan</h4>
        <p>"Simple transfers and honest rates, I would not send money any other way now."</p>
      </div>
      <div class="quote">
        <div class="avatar" role="img" aria-label="Portrait photo of customer Priya Holm"></div>
        <h4>Priya holm</h4>
        <p>"Fast, friendly and clear. My family abroad gets their money the very next day."</p>
      </div>
      <div class="quote">
        <div class="avatar" role="img" aria-label="Portrait photo of customer Dana Vorst"></div>
        <h4>Dana vorst</h4>
        <p>"The fees are lower than my bank and the whole process took only minutes."</p>
      </div>
      <div class="quote">
        <div class="avatar" role="img" aria-label="Portrait photo of customer Ilse Moran"></div>
        <h4>Ilse moran</h4>
        <p>"Great support team and a service that always does exactly what it promises."</p>
      </div>
    </div>
    <span class="btn">Get started</span>
  </section>

  <section class="stats">
    <h2 class="section-title">What we achived last year</h2>
    <p class="section-intro">Lorem ipsum dolor sit amet, consectetur adipiscing elit, sed do eiusmod tempor incididunt ut labore et dolore magna aliqua.</p>
    <div class="stats-body">
      <ul class="stats-list">
        <li>100% Satisfied Customers</li>
        <li>2000+ New clients every day</li>
        <li>Top and responsive firm in the world</li>
        <li>100% Successful transactions</li>
        <li>Millions of smiles</li>
      </ul>
      <svg class="rate-chart" width="460" height="260" viewBox="0 0 460 260" font-family="Open Sans, sans-serif" font-size="10" fill="#7a7f85">
        <g stroke="#e3e6e9" stroke-width="1">
          <line x1="60" y1="20" x2="450" y2="20"/><line x1="60" y1="60" x2="450" y2="60"/>
          <line x1="60" y1="100" x2="450" y2="100"/><line x1="60" y1="140" x2="450" y2="140"/>
          <line x1="60" y1="180" x2="450" y2="180"/><line x1="60" y1="220" x2="450" y2="220"/>
        </g>
        <text x="50" y="24" text-anchor="end">0.8350</text><text x="50" y="64" text-anchor="end">0.8300</text>
        <text x="50" y="104" text-anchor="end">0.8250</text><text x="50" y="144" text-anchor="end">0.8200</text>
        <text x="50" y="184" text-anchor="end">0.8150</text><text x="50" y="224" text-anchor="end">0.8100</text>
        <text x="70" y="244">01.02.2015</text><text x="170" y="244">01.04.2015</text>
        <text x="270" y="244">01.06.2015</text><text x="370" y="244">01.08.2015</text>
        <polyline fill="none" stroke="#1aa0d8" stroke-width="2.5" points="62,200 90,150 110,180 130,120 150,160 170,110 195,140 215,90 240,120 260,100 285,130 305,95 330,115 355,80 380,100 405,70 430,40 450,22"/>
      </svg>
    </div>
  </section>

  <section class="world">
    <h2 class="section-title">Trusted all over the world</h2>
    <p class="section-intro">Lorem ipsum dolor sit amet, consectetur adipiscing elit, sed do eiusmod tempor incididunt.</p>
    <div class="world-map" role="img" aria-label="Dotted world map illustration"></div>
  </section>

  <footer class="footer">
    <span>© Copyright 2015. All Rights Reserved by Sendora</span>
    <div class="social"><i></i><i></i><i></i><i></i></div>
  </footer>

</div>
</body>
</html>
```